Need A Modern Website Design For ADSL2+ Provider

AIM: To sell affordable combined ADSL2+ Unlimited & phone line rentals to residential customers.

TYPE: This project is for DESIGN only (no code)

Source Files: I need all source files, fonts, images to be provided in ZIP format.

Logo: Existing (attached)

-Corporate Colours-
Black & Red (Same as Logo)
Others colours are fine as long as it looks corporate and modern.

-Pages-
Need another page to display our pricing plan

(1)Homepage Design
(2)Page to display our plans (needs to be in tables)
Example: http://lnkbrev.example/QwTr8k

-Pricing Plan-
(1) $59.95 / Month (Metro / City Areas)
(2) $79.95 / Month (Outside City Areas / Rural Areas)
Detailed Pricing plans is in PDF attached
Updates

Target Market(s)

Both male & female, Young & Old

Industry/Entity Type

Residential

Requirements
Must have
• + Graphic banner on the home page that shows our ADSL2+ combo plan for ADSL2+ Unlimited & Phone Line Rental for only $59.95

+ A box to allow customers to login to their account (username & password + login button)

+ Clearly display contact number
+ Button to sign up
+ Button to check service availability something like https://checkin.pelwara.example/wizard/

+ Button for Live Chat
+ Navigation menu
+ Social media icons Facebook, Google +, Twitter
+ Minimal text on homepage
+ Corporate & Friendly
Nice to have
• + Effective use of icons with corporate colours
+ Effective use of stockphotos
(use of people in photos would be nice)

+ Effective use of graphics to navigate people through the site and inform customers of specials,etc.
Should not have
• + Cluttered
+ Don’t want long scrolling homepage
+ Don’t want too much text on homepage 500 words is the estimate max.

```html
<!DOCTYPE html>
<html lang="en">
<head>
<meta charset="utf-8">
<title>Corvane — ADSL2+ Unlimited &amp; Phone Line Rental</title>
<link rel="stylesheet" href="https://fonts.googleapis.com/css2?family=Open+Sans:ital,wght@0,400;0,600;0,700;1,400&family=Roboto+Slab:wght@400;700&display=swap">
<style>
:root{
  --red:#ee3e33;
  --red-dark:#d8322a;
  --ink:#444444;
  --text:#777777;
  --dark:#333333;
  --dark-btn:#444444;
  --soft:#f4f4f4;
  --white:#ffffff;
  --footer-text:#888888;
  --footer-line:#444444;
}
*{box-sizing:border-box;margin:0;padding:0}
html,body{width:1200px;height:1159px;overflow:hidden}
body{position:relative;background:var(--white);font-family:"Open Sans",Arial,sans-serif;color:var(--text)}
.abs{position:absolute}

/* header */
.site-header{position:absolute;left:0;top:0;width:1200px;height:52px;background:var(--white)}
.brand{position:absolute;left:300px;top:10px;display:flex;align-items:center;gap:8px}
.brand-dot{width:32px;height:32px;border-radius:50%;background:#111}
.brand-name{font-family:"Roboto Slab",Georgia,serif;font-weight:400;font-size:26px;letter-spacing:1px;color:#111}
.main-nav a{position:absolute;top:32px;font-size:9px;color:#333;text-decoration:none;text-transform:uppercase}
.main-nav .is-active{left:509px;top:0;width:44px;height:52px;background:var(--red);color:var(--white);text-align:center;padding-top:33px}
.header-call{position:absolute;left:787px;top:11px;font-size:9px;color:#555;display:flex;align-items:center;gap:5px}
.pill{position:absolute;top:30px;height:16px;font-size:9px;color:var(--white);text-align:center;line-height:16px;border-radius:2px;text-transform:uppercase}
.pill-login{left:791px;width:47px;background:var(--red)}
.pill-signup{left:849px;width:46px;background:#333}

/* hero */
.hero{position:absolute;left:0;top:52px;width:1200px;height:323px;background:#000;overflow:hidden}
.hero-photo{position:absolute;left:230px;top:0;width:740px;height:323px;
  background:radial-gradient(ellipse at 62% 45%,#b9a48a 0%,#7c7266 30%,#3d3a37 60%,#000 100%)}
.hero-copy{position:absolute;left:300px;top:16px;font-family:"Roboto Slab",Georgia,serif;font-weight:700;font-size:40px;line-height:45px;color:var(--white);text-transform:uppercase;text-shadow:0 2px 3px rgba(0,0,0,.5)}
.hero-copy .accent{color:var(--red)}
.hero-copy .price{font-size:46px}
.hero-rule{position:absolute;left:300px;top:253px;width:581px;height:1px;background:#cfcfcf}
.hero-call{position:absolute;left:300px;top:266px;font-family:"Roboto Slab",Georgia,serif;font-weight:700;font-size:30px;color:var(--white);text-shadow:0 2px 3px rgba(0,0,0,.5)}
.hero-call .accent{color:var(--red)}

/* sections */
.section-title{position:absolute;left:0;width:1200px;text-align:center;font-family:"Roboto Slab",Georgia,serif;font-weight:700;font-size:23px;color:var(--ink);text-transform:uppercase}
.section-copy{position:absolute;left:316px;width:568px;text-align:center;font-size:9.4px;line-height:14.5px;color:var(--text)}

.welcome{position:absolute;left:0;top:375px;width:1200px;height:133px;background:#fbfbfb}
.account{position:absolute;left:0;top:508px;width:1200px;height:149px;background:var(--red)}
.account .section-title{color:var(--white);top:22px}
.field{position:absolute;top:67px;width:184px;height:21px;background:#f7f7f7;border:1px solid #ddd;border-radius:2px;font-size:8px;color:#aaa;padding:5px 4px}
.btn-light{position:absolute;top:106px;height:22px;font-size:8px;font-weight:700;text-align:center;line-height:22px;border-radius:2px;text-transform:uppercase}
.btn-signup{left:544px;width:52px;background:#fbe4e2;color:var(--red)}
.btn-login{left:607px;width:51px;border:2px solid var(--white);color:var(--white);line-height:18px}

.plans-intro{position:absolute;left:0;top:657px;width:1200px;height:183px;background:#fbfbfb}
.btn-red{position:absolute;left:560px;top:125px;width:81px;height:32px;background:var(--red);color:var(--white);font-size:10px;font-weight:700;text-align:center;line-height:32px;border-radius:2px}

.availability{position:absolute;left:0;top:840px;width:1200px;height:138px;background:var(--soft)}
.phone-box{position:absolute;left:351px;top:76px;width:56px;height:32px;background:var(--red);display:flex;align-items:center;justify-content:center}
.phone-box::after{content:"";position:absolute;right:-5px;top:12px;border-left:5px solid var(--red);border-top:4px solid transparent;border-bottom:4px solid transparent}
.phone-field{position:absolute;left:407px;top:76px;width:350px;height:32px;background:var(--white);border:1px solid #ccc;font-size:12px;font-style:italic;color:#aaa;padding:7px 12px}
.btn-dark{position:absolute;left:763px;top:76px;width:80px;height:32px;background:var(--dark-btn);color:var(--white);font-size:10.5px;font-weight:700;text-align:center;line-height:32px;border-radius:2px}

/* footer */
.site-footer{position:absolute;left:0;top:978px;width:1200px;height:181px;background:var(--dark)}
.footer-title{position:absolute;top:20px;font-size:12px;color:var(--footer-text)}
.footer-about{position:absolute;left:338px;top:52px;width:185px;font-size:8px;line-height:12px;color:#6e6e6e}
.footer-list{position:absolute;list-style:none;width:145px}
.footer-list li{font-size:8px;color:#7a7a7a;height:24.5px;padding-top:4px;border-bottom:1px solid var(--footer-line);display:flex;gap:6px;align-items:flex-start}
.footer-list li:last-child{border-bottom:none}
.social{position:absolute;left:746px;top:101px;display:flex;gap:5px}
.social span{width:16px;height:16px;border-radius:50%;background:#5a5a5a}
.footer-rule{position:absolute;left:275px;top:148px;width:650px;height:1px;background:#3f3f3f}
.copyright{position:absolute;left:336px;top:160px;font-size:7.5px;color:#6e6e6e}
</style>
</head>
<body>

<header class="site-header">
  <div class="brand"><span class="brand-dot"></span><span class="brand-name">CORVANE</span></div>
  <nav class="main-nav">
    <a class="is-active" href="#">Home</a>
    <a href="#" style="left:572px">Pricing Plan</a>
    <a href="#" style="left:657px">Support</a>
    <a href="#" style="left:722px">Contact Us</a>
  </nav>
  <div class="header-call">
    <svg width="11" height="11" viewBox="0 0 24 24"><path fill="#444" d="M6.6 10.8c1.4 2.8 3.8 5.1 6.6 6.6l2.2-2.2c.3-.3.7-.4 1-.2 1.1.4 2.3.6 3.6.6.6 0 1 .4 1 1V20c0 .6-.4 1-1 1C10.6 21 3 13.4 3 4c0-.6.4-1 1-1h3.5c.6 0 1 .4 1 1 0 1.3.2 2.5.6 3.6.1.3 0 .7-.2 1z"/></svg>
    <span>CALL US:&nbsp; 1300 55 01 99</span>
  </div>
  <span class="pill pill-login">Login</span>
  <span class="pill pill-signup">Sign Up</span>
</header>

<section class="hero">
  <div class="hero-photo" role="img" aria-label="Stock photo of a smiling customer on the phone at a home desk with a computer monitor"></div>
  <h1 class="hero-copy">
    <span class="accent">ADSL2+</span><br>
    Unlimited <span class="accent">&amp;</span><br>
    <span class="accent">Phone</span> Line<br>
    Rental For<br>
    <span class="accent">Only <span class="price">$59.95</span></span>
  </h1>
  <div class="hero-rule"></div>
  <div class="hero-call">CALL US : <span class="accent">1300 55 01 99</span></div>
</section>

<section class="welcome">
  <h2 class="section-title" style="top:18px">Welcome to our site</h2>
  <p class="section-copy" style="top:62px">Lorem ipsum dolor sit amet, consectetur adipisicing elit, sed do eiusmod tempor incididunt ut labore et dolore magna aliqua. Ut enim ad minim veniam, quis nostrud exercitation ullamco laboris nisi ut aliquip ex ea commodo consequat. Duis aute irure dolor in reprehenderit in voluptate velit esse cillum dolore eu fugiat nulla pariatur.</p>
</section>

<section class="account">
  <h2 class="section-title">Sign up/Login here</h2>
  <div class="field" style="left:413px">Username</div>
  <div class="field" style="left:605px">Password</div>
  <span class="btn-light btn-signup">Sign Up</span>
  <span class="btn-light btn-login">Login</span>
</section>

<section class="plans-intro">
  <h2 class="section-title" style="top:25px">About our pricing plans</h2>
  <p class="section-copy" style="top:65px">Lorem ipsum dolor sit amet, consectetur adipisicing elit, sed do eiusmod tempor incididunt ut labore et dolore magna aliqua. Ut enim ad minim veniam, quis nostrud exercitation ullamco laboris nisi ut aliquip ex ea commodo consequat. Duis aute irure dolor in reprehenderit in voluptate velit esse cillum dolore eu fugiat nulla pariatur.</p>
  <span class="btn-red">Learn More</span>
</section>

<section class="availability">
  <h2 class="section-title" style="top:22px">Check service availabality</h2>
  <div class="phone-box">
    <svg width="26" height="26" viewBox="0 0 24 24"><path fill="#fff" d="M6.6 10.8c1.4 2.8 3.8 5.1 6.6 6.6l2.2-2.2c.3-.3.7-.4 1-.2 1.1.4 2.3.6 3.6.6.6 0 1 .4 1 1V20c0 .6-.4 1-1 1C10.6 21 3 13.4 3 4c0-.6.4-1 1-1h3.5c.6 0 1 .4 1 1 0 1.3.2 2.5.6 3.6.1.3 0 .7-.2 1z"/></svg>
  </div>
  <div class="phone-field">Enter your phone number</div>
  <span class="btn-dark">View Plans</span>
</section>

<footer class="site-footer">
  <h3 class="footer-title" style="left:338px">Corvane</h3>
  <p class="footer-about">Sed ut perspiciatis unde omnis iste natus error sit voluptatem accusantium doloremque laudantium, totam rem aperiam, eaque ipsa quae ab illo inventore veritatis et quasi architecto beatae vitae dicta sunt explicabo.</p>

  <h3 class="footer-title" style="left:561px">Useful Links</h3>
  <ul class="footer-list" style="left:561px;top:48px">
    <li>Home</li><li>Pricing Plan</li><li>Support</li><li>Terms &amp; Conditions</li>
  </ul>

  <h3 class="footer-title" style="left:747px">Contact Us</h3>
  <ul class="footer-list" style="left:746px;top:48px">
    <li><svg width="8" height="8" viewBox="0 0 24 24"><path fill="#6a6a6a" d="M6.6 10.8c1.4 2.8 3.8 5.1 6.6 6.6l2.2-2.2c.3-.3.7-.4 1-.2 1.1.4 2.3.6 3.6.6.6 0 1 .4 1 1V20c0 .6-.4 1-1 1C10.6 21 3 13.4 3 4c0-.6.4-1 1-1h3.5c.6 0 1 .4 1 1 0 1.3.2 2.5.6 3.6.1.3 0 .7-.2 1z"/></svg>1300 55 01 99</li>
    <li><svg width="9" height="8" viewBox="0 0 24 18"><path fill="#6a6a6a" d="M0 0h24v18H0zM2 2v1l10 7 10-7V2z"/></svg>www.corvane.example</li>
  </ul>
  <div class="social" aria-label="Social media links"><span></span><span></span><span></span><span></span></div>

  <div class="footer-rule"></div>
  <p class="copyright">Copyright © 2013 Corvane. All Rights Reserved.</p>
</footer>

</body>
</html>
```